Business Card for Property Management Firm
Halvorsen Crest Property Management
Creative Brief
Professional
Dean Olwright
Broker
7182 Marbury Lane Los Alamitos Ca 90731
dean@hcpmxv.com
www.HCPropertymanagement.example
Please include the following items to be highlighted on the other folds of the business cards if they fit 1.) Top 1% of Leasing Brokerages in Southern California 2.) Ranked Top 5 Leasing Agents in Orange County 3 Years Running 3.) "Proudly Managing Over 100 Million in Real Estate Assets" 4.) If room permits you can also add: HCPM - Residential Property Management Solutions
see comments above

```html
<!DOCTYPE html>
<html lang="en">
<head>
<meta charset="utf-8">
<title>Halvorsen Crest Property Management — Business Card</title>
<link href="https://fonts.googleapis.com/css2?family=Open+Sans:wght@400;600;700&display=swap" rel="stylesheet">
<style>
  :root {
    --page: #e7e6e2;
    --card: #fbfbfa;
    --card-shade: #e9e9e7;
    --green: #3e5a51;
    --green-dark: #2c433c;
    --ink: #3a3a3a;
    --ink-soft: #6b6b6b;
    --on-green: #f2f4f3;
  }
  * { box-sizing: border-box; margin: 0; padding: 0; }
  html, body { width: 1200px; height: 959px; overflow: hidden; }
  body {
    background: var(--page);
    font-family: "Open Sans", Arial, sans-serif;
    color: var(--ink);
    position: relative;
  }
  .card {
    position: absolute;
    top: 150px;
    width: 380px;
    height: 660px;
    background: linear-gradient(160deg, var(--card) 0%, var(--card) 55%, var(--card-shade) 100%);
    box-shadow: 0 6px 18px rgba(0,0,0,0.18);
    overflow: hidden;
  }
  .card--back { left: 170px; }
  .card--front { left: 650px; }

  /* back */
  .back-mark {
    position: absolute;
    left: 70px; top: 150px;
    width: 120px; height: 120px;
    background: var(--green);
  }
  .back-monogram {
    position: absolute;
    left: 70px; top: 284px;
    font-size: 22px; font-weight: 600;
    letter-spacing: 4px;
    color: var(--green);
  }
  .back-band {
    position: absolute;
    left: 190px; top: 228px;
    right: 0; height: 42px;
    background: var(--green);
    display: flex; align-items: center;
    padding: 0 10px;
  }
  .back-band span {
    font-size: 8.5px; color: var(--on-green); letter-spacing: 0.2px; white-space: nowrap;
  }

  /* front */
  .brand {
    position: absolute;
    left: 44px; top: 120px;
    display: flex; align-items: center; gap: 12px;
  }
  .brand-square { width: 46px; height: 46px; background: var(--green); flex: none; }
  .brand-name {
    font-size: 14px; font-weight: 600; line-height: 1.25;
    color: var(--green); text-transform: uppercase; letter-spacing: 1px;
  }
  .tagline-band {
    position: absolute;
    left: 102px; right: 0; top: 174px; height: 14px;
    background: var(--green);
    display: flex; align-items: center; padding-left: 8px;
  }
  .tagline-band span {
    font-size: 7px; color: var(--on-green); letter-spacing: 0.8px; text-transform: uppercase; white-space: nowrap;
  }
  .name-tab {
    position: absolute; left: 0; top: 322px;
    width: 38px; height: 46px; background: var(--green);
  }
  .person { position: absolute; left: 52px; top: 324px; }
  .person-name { font-size: 14px; font-weight: 600; letter-spacing: 0.5px; text-transform: uppercase; }
  .person-role { font-size: 10.5px; color: var(--ink-soft); margin-top: 2px; }

  .icon-rail {
    position: absolute; left: 0; top: 412px;
    width: 34px; height: 220px;
    background: var(--green-dark);
    display: flex; flex-direction: column; align-items: center;
    padding-top: 12px; gap: 17px;
  }
  .icon-rail svg { width: 14px; height: 14px; fill: none; stroke: var(--on-green); stroke-width: 1.6; }
  .contact-list {
    position: absolute; left: 52px; top: 422px; right: 16px;
    list-style: none; font-size: 10.5px; color: var(--ink);
    display: flex; flex-direction: column; gap: 16.5px;
  }
  .contact-list li { white-space: nowrap; }
</style>
</head>
<body>

<section class="card card--back" aria-label="Business card back">
  <div class="back-mark"></div>
  <div class="back-band"><span>www.HCPropertymanagement.example</span></div>
  <div class="back-monogram">HCPM</div>
</section>

<section class="card card--front" aria-label="Business card front">
  <div class="brand">
    <div class="brand-square"></div>
    <div class="brand-name">Halvorsen Crest<br>Property Management</div>
  </div>
  <div class="tagline-band"><span>Residential Property Management Solutions</span></div>

  <div class="name-tab"></div>
  <div class="person">
    <div class="person-name">Dean Olwright</div>
    <div class="person-role">Broker</div>
  </div>

  <div class="icon-rail">
    <svg viewBox="0 0 16 16"><path d="M4 1.5h3l1 3.5-2 1.2a8 8 0 0 0 3.8 3.8l1.2-2 3.5 1v3a1.5 1.5 0 0 1-1.5 1.5A12 12 0 0 1 2.5 3 1.5 1.5 0 0 1 4 1.5z"/></svg>
    <svg viewBox="0 0 16 16"><rect x="4" y="1.5" width="8" height="13" rx="1.5"/><line x1="7" y1="12" x2="9" y2="12"/></svg>
    <svg viewBox="0 0 16 16"><rect x="2" y="6" width="12" height="7"/><rect x="4.5" y="2" width="7" height="4"/><line x1="5" y1="10" x2="11" y2="10"/></svg>
    <svg viewBox="0 0 16 16"><rect x="1.5" y="3.5" width="13" height="9"/><path d="M1.5 3.5 8 9l6.5-5.5"/></svg>
    <svg viewBox="0 0 16 16"><circle cx="8" cy="8" r="6.5"/><ellipse cx="8" cy="8" rx="2.8" ry="6.5"/><line x1="1.5" y1="8" x2="14.5" y2="8"/></svg>
    <svg viewBox="0 0 16 16"><path d="M8 15s5-5 5-8.5a5 5 0 0 0-10 0C3 10 8 15 8 15z"/><circle cx="8" cy="6.5" r="1.8"/></svg>
  </div>
  <ul class="contact-list">
    <li>010 555 0142</li>
    <li>010 555 0142</li>
    <li>010 555 0142</li>
    <li>dean@hcpmxv.com</li>
    <li>www.HCPropertymanagement.example</li>
    <li>7182 Marbury Lane Los Alamitos Ca 90731</li>
  </ul>
</section>

</body>
</html>
```